Church Music Album Cover

We are a Christian church in the OKC metro that is releasing a CD of songs that have connected with our congregation over the past few years. We are a church of about 1500 people of all ages- so while we want the design to be fresh, clean, and attractive- it doesn't have to be overly "youthy" or "edgy." Per the CD distribution company, the art image file you create should be able to be delivered with these requirements met:1400 x 1400 pixels minimum; 3000 x 3000 pixels maximumPNG, GIF, JPG, or JPEG file type72 - 300dpi (300dpi is the best)Less than 25mbRGB color scheme (not CMYK)
Updates

Thanks for submissions thus far. I realize my initial description may have not been the most helpful- and it some ways, I'm not 100% sure what I want. However, I would typically end to stay away from concrete images and tend to lean more towards earthy folk images. I don't even know if that makes sense. One google image search of the word "Grace" brings up individual letters spelling out Grace- each on a card clothes lined to a rope with out of focus lights or candles in the background. Another one had out of focus patio light bulbs lighting up the general text. Not sure why I like those and how they can connect to the theme, but I do. Another one had "Grace" on a pallet wall type background. Hopefully those are helpful suggestions.

Target Market(s)

Young parents- 30-40's

Colors

Requirements
Must have
• Title: Melodies from the River Stone
Nice to have
• Earthy/folky themes.
Should not have
• Bright colors

```html
<!DOCTYPE html>
<html lang="en">
<head>
<meta charset="utf-8">
<title>Melodies from the River Stone – Album Cover</title>
<link rel="stylesheet" href="https://fonts.googleapis.com/css2?family=Questrial&display=swap">
<style>
  :root {
    --sky-high: #4f6f82;
    --sky-mid: #6d8a98;
    --sky-haze: #a9b5b0;
    --sun-glow: #efe8d8;
    --sun-warm: rgba(214, 198, 168, 0.55);
    --ridge: #5d6f6c;
    --hills: #4b6470;
    --water: #3f5a68;
    --water-light: #7f929a;
    --title: #f6f2ea;
  }
  * { margin: 0; padding: 0; box-sizing: border-box; }
  html, body {
    width: 1200px;
    height: 1200px;
    overflow: hidden;
  }
  body {
    background: var(--sky-high);
    font-family: "Questrial", "Century Gothic", sans-serif;
  }
  .album-cover {
    position: relative;
    width: 1200px;
    height: 1200px;
    overflow: hidden;
  }
  .cover-scene {
    position: absolute;
    inset: 0;
    background:
      radial-gradient(circle at 26% 33%, var(--sun-glow) 0%, rgba(239,232,216,0.8) 7%, var(--sun-warm) 20%, rgba(214,198,168,0) 42%),
      radial-gradient(ellipse 60% 18% at 70% 62%, rgba(196,200,188,0.45) 0%, rgba(196,200,188,0) 100%),
      linear-gradient(180deg,
        var(--sky-high) 0%,
        var(--sky-mid) 34%,
        var(--sky-haze) 56%,
        var(--ridge) 66%,
        var(--hills) 74%,
        var(--water) 86%,
        var(--water-light) 100%);
  }
  .album-title {
    position: absolute;
    left: 0;
    right: 0;
    top: 950px;
    text-align: center;
    color: var(--title);
    font-size: 52px;
    font-weight: 400;
    letter-spacing: 1px;
    text-transform: uppercase;
    line-height: 1;
    white-space: nowrap;
  }
</style>
</head>
<body>
  <main class="album-cover">
    <div class="cover-scene" role="img" aria-label="Photograph of a soft sun in a hazy cloudy sky, a small flock of birds, a lone tree on a mountain ridge, reflected in calm water"></div>
    <h1 class="album-title">Melodies from the River Stone</h1>
  </main>
</body>
</html>
```